TR Stationery - Modern Contemporary

Develop modern template for Letterhead and Stationery (business card, letterhead, envelopes) using the TR Logo and Icon

Colors
0054AA
0677BA
7BADD7
CADEEF
E8F1F8
00AB8E
00BBA5
67D7C9
C6EFE9
E9F9F6
EE7325
F08F49
F5BC92
FAE3D3
FDF4ED
6B429C
8869AF
B7A5CE
E3DAEB
F3F0F8

```html
<!DOCTYPE html>
<html lang="en">
<head>
<meta charset="utf-8">
<title>TR Stationery</title>
<link rel="stylesheet" href="https://fonts.googleapis.com/css2?family=Playfair+Display:wght@400&family=Montserrat:wght@400;600;800&display=swap">
<style>
  :root{
    --backdrop:#cadeef;
    --paper:#f3f0f8;
    --blue:#0054aa;
    --green:#00ab8e;
    --orange:#ee7325;
    --purple:#6b429c;
    --ink:#2b2b33;
    --faint-green:#c6efe9;
  }
  *{box-sizing:border-box;margin:0;padding:0}
  html,body{width:1200px;height:900px;overflow:hidden}
  body{background:var(--backdrop);position:relative;font-family:"Montserrat",sans-serif;color:var(--ink)}
  address{font-style:normal}
  .sheet{position:absolute;background:var(--paper);box-shadow:0 6px 18px rgba(0,84,170,.15)}
  .wordmark{font-family:"Playfair Display",serif;font-weight:400;color:var(--blue);letter-spacing:1px;line-height:1}

  /* Letterhead */
  .letterhead{left:40px;top:40px;width:580px;height:820px}
  .letterhead .top-bar{position:absolute;left:60px;top:0;width:240px;height:9px;background:var(--blue)}
  .letterhead .wordmark{position:absolute;left:60px;top:110px;font-size:46px}
  .letterhead .address{position:absolute;right:50px;top:45px;text-align:right;font-size:12px;font-weight:600;line-height:1.45;text-transform:uppercase}
  .letterhead .address .web{text-transform:none}
  .letterhead h1{position:absolute;left:60px;top:250px;font-size:15px;font-weight:800;letter-spacing:4px}
  .letterhead .body-text{position:absolute;left:60px;top:285px;width:460px;font-size:12px;line-height:1.5;text-align:justify}
  .letterhead .closing{position:absolute;left:60px;top:590px;width:250px;font-size:12px;line-height:1.5}
  .letterhead .signature{position:absolute;left:200px;top:675px;font-size:12px;font-weight:800;letter-spacing:3px}
  .letterhead .faint-mark{position:absolute;left:60px;bottom:40px;width:90px;height:90px;border-radius:50%;background:var(--faint-green)}
  .accent-row{position:absolute;display:flex;align-items:center;gap:8px}
  .dot{width:16px;height:16px;border-radius:50%}
  .dot.green{background:var(--green)} .dot.blue{background:var(--blue)} .dot.orange{background:var(--orange)}
  .rule{height:6px;background:var(--blue)}
  .letterhead .accent-row{right:40px;bottom:60px}
  .letterhead .accent-row .rule{width:100px}

  /* Envelope */
  .envelope{left:650px;top:40px;width:510px;height:265px;overflow:hidden}
  .envelope .flap{position:absolute;inset:0}
  .envelope .top-rule{position:absolute;right:30px;top:92px;width:190px;height:5px;background:var(--blue)}
  .envelope .wordmark{position:absolute;right:30px;top:112px;font-size:26px}
  .envelope .address{position:absolute;right:215px;top:160px;text-align:right;font-size:7.5px;font-weight:600;line-height:1.4;text-transform:uppercase}
  .envelope .contact{position:absolute;right:215px;top:200px;font-size:7.5px;font-weight:600;line-height:1.4;text-align:right}
  .envelope .accent-row{left:0;bottom:22px}
  .envelope .accent-row .rule{width:60px;height:4px}
  .envelope .dot{width:13px;height:13px}

  /* Business cards */
  .card{width:300px;height:172px}
  .card-front{left:650px;top:370px}
  .card-front .wordmark{position:absolute;left:0;right:0;top:68px;text-align:center;font-size:36px}
  .card-back{left:860px;top:580px;background:var(--orange);color:#fff}
  .card-back .wordmark{position:absolute;right:24px;top:24px;font-size:28px;color:#fff}
  .card-back .name{position:absolute;left:24px;top:88px;font-size:10px;font-weight:800;letter-spacing:2.5px;color:var(--ink)}
  .card-back .details{position:absolute;left:24px;top:106px;font-size:8px;line-height:1.45;text-transform:uppercase}
  .card-back .details .web{text-transform:none}
</style>
</head>
<body>

<section class="sheet letterhead">
  <div class="top-bar"></div>
  <div class="wordmark">TR</div>
  <address class="address">
    48 Alder Lane<br>Suite 3C<br>Northfield<br>+1 555 0148 220<br><span class="web">www.trstudio.co</span>
  </address>
  <h1>LETTERHEAD</h1>
  <p class="body-text">Lorem ipsum dolor sit amet, consectetur adipisicing elit, sed do eiusmod tempor incididunt ut labore et dolore magna aliqua. Ut enim ad minim veniam, quis nostrud exercitation ullamco laboris nisi ut aliquip ex ea commodo consequat. Duis aute irure dolor in reprehenderit in voluptate velit esse cillum dolore eu fugiat nulla pariatur. Excepteur sint occaecat cupidatat non proident, sunt in culpa qui officia deserunt mollit anim id est laborum. Sed ut perspiciatis unde omnis iste natus error sit voluptatem accusantium doloremque laudantium, totam rem aperiam, eaque ipsa quae ab illo inventore veritatis et quasi architecto beatae vitae dicta sunt explicabo. Nemo enim ipsam voluptatem quia voluptas sit aspernatur aut odit aut fugit, sed quia consequuntur magni dolores eos qui ratione voluptatem sequi nesciunt. Neque porro quisquam est, qui dolorem ipsum quia dolor sit amet, consectetur, adipisci velit, sed quia non numquam eius modi tempora incidunt ut labore et dolore magnam aliquam quaerat voluptatem.</p>
  <p class="closing">Lorem ipsum dolor sit amet, consectetur adipisicing elit, sed do eiusmod tempor incididunt ut labore et dolore magna aliqua.</p>
  <div class="signature">LENA VARGA</div>
  <div class="faint-mark"></div>
  <div class="accent-row">
    <span class="dot green"></span><span class="dot blue"></span><span class="dot orange"></span><span class="rule"></span>
  </div>
</section>

<section class="sheet envelope">
  <svg class="flap" viewBox="0 0 510 265" aria-hidden="true">
    <polyline points="0,0 0,70 30,85 450,0" fill="none" stroke="#d8d2e4" stroke-width="1.5"/>
  </svg>
  <div class="top-rule"></div>
  <div class="wordmark">TR</div>
  <address class="address">48 Alder Lane<br>Suite 3C<br>Northfield</address>
  <div class="contact">+1 555 0148 220<br>www.trstudio.co</div>
  <div class="accent-row">
    <span class="rule"></span><span class="dot orange"></span><span class="dot blue"></span><span class="dot green"></span>
  </div>
</section>

<section class="sheet card card-front">
  <div class="wordmark">TR</div>
</section>

<section class="sheet card card-back">
  <div class="wordmark">TR</div>
  <div class="name">LENA VARGA</div>
  <address class="details">48 Alder Lane<br>Suite 3C<br>Northfield<br>+1 555 0148 220<br><span class="web">www.trstudio.co</span></address>
</section>

</body>
</html>
```